Kestrel Valley Alpine Riders Society needs a business card design

We need a business card design for our newly incorporated KVARS. We are helping the NZ Chinese community, as well as everyone else, to organise ski & snowboarding trips, training, and equipments. The design should be creative, energetic, young and vibrant.

Industry/Entity Type

Social Club

Contact Information for Business Card

Logo; Kestrel Valley Alpine Riders Society; Name: Oliver Brandt; Position: President; Address: 42 Marwick Rd, Epsom, Auckland 1051; Mobile: 020 7826 1957; Email: oliver@kvars-club.example; Web: www.kvars-club.example

Requirements
Must have
• 1, The text "Kestrel Valley Alpine Riders Society" should be put together with the supplied logo file to form a new complete logo combination.
• 2, Final design files should be in Adobe Illustrator format and all text must be editable.
Nice to have
• two or three colours

```html
<!DOCTYPE html>
<html lang="en">
<head>
<meta charset="utf-8">
<title>KVARS Business Card</title>
<link rel="stylesheet" href="https://fonts.googleapis.com/css2?family=Roboto:wght@400;500;700;900&display=swap">
<style>
  :root {
    --backdrop: #e6e6e6;
    --card-light: #2cc3ee;
    --card-deep: #06afe3;
    --ink-white: #ffffff;
    --ink-soft: rgba(255, 255, 255, 0.92);
    --mark-circle: #1f3f9a;
    --shadow: rgba(0, 0, 0, 0.22);
  }
  * { margin: 0; padding: 0; box-sizing: border-box; }
  html, body {
    width: 1200px;
    height: 900px;
    overflow: hidden;
    background: var(--backdrop);
    font-family: "Roboto", Arial, sans-serif;
  }
  .sheet {
    width: 1200px;
    height: 900px;
    display: flex;
    flex-direction: column;
    align-items: center;
    justify-content: center;
    gap: 44px;
  }
  .card {
    position: relative;
    width: 700px;
    height: 400px;
    background: linear-gradient(160deg, var(--card-light) 0%, var(--card-deep) 100%);
    box-shadow: 0 6px 18px var(--shadow);
    color: var(--ink-white);
    overflow: hidden;
  }
  .lockup {
    display: flex;
    flex-direction: column;
    align-items: center;
    gap: 10px;
  }
  .brand {
    display: flex;
    align-items: center;
    gap: 16px;
  }
  .brand-dot {
    width: 46px;
    height: 46px;
    border-radius: 50%;
    background: var(--mark-circle);
  }
  .brand-name {
    font-weight: 900;
    font-size: 92px;
    letter-spacing: 2px;
    line-height: 1;
    color: var(--ink-white);
  }
  .brand-full {
    font-weight: 700;
    font-size: 16px;
    letter-spacing: 1px;
    line-height: 1.2;
    color: var(--ink-white);
    white-space: nowrap;
  }
  /* Front */
  .card-front .lockup {
    position: absolute;
    left: 50%;
    top: 100px;
    transform: translateX(-50%);
  }
  .card-front .web {
    position: absolute;
    left: 0;
    right: 0;
    top: 300px;
    text-align: center;
    font-weight: 700;
    font-size: 17px;
    letter-spacing: 3px;
  }
  /* Back */
  .card-back .lockup {
    position: absolute;
    left: 60px;
    top: 212px;
    gap: 8px;
  }
  .card-back .brand-name { font-size: 68px; }
  .card-back .brand-dot { width: 36px; height: 36px; }
  .card-back .brand-full { font-size: 12px; letter-spacing: 0.8px; }
  .contact {
    position: absolute;
    left: 432px;
    top: 70px;
  }
  .contact-name {
    font-weight: 700;
    font-size: 25px;
    letter-spacing: 0.5px;
    text-transform: uppercase;
  }
  .contact-role {
    font-weight: 500;
    font-size: 12px;
    letter-spacing: 2px;
    text-transform: uppercase;
    margin-top: 2px;
    margin-bottom: 14px;
  }
  .contact-lines,
  .contact-address {
    font-size: 14px;
    line-height: 1.5;
    letter-spacing: 1px;
    color: var(--ink-soft);
  }
  .contact-address { margin-top: 12px; }
</style>
</head>
<body>
  <main class="sheet">
    <section class="card card-front" aria-label="Business card front">
      <div class="lockup">
        <div class="brand">
          <span class="brand-dot"></span>
          <span class="brand-name">KVARS</span>
        </div>
        <p class="brand-full">Kestrel Valley Alpine Riders Society</p>
      </div>
      <p class="web">www.kvars-club.example</p>
    </section>

    <section class="card card-back" aria-label="Business card back">
      <div class="lockup">
        <div class="brand">
          <span class="brand-dot"></span>
          <span class="brand-name">KVARS</span>
        </div>
        <p class="brand-full">Kestrel Valley Alpine Riders Society</p>
      </div>
      <div class="contact">
        <p class="contact-name">Oliver Brandt</p>
        <p class="contact-role">President</p>
        <div class="contact-lines">
          <p>020 7826 1957</p>
          <p>oliver@kvars-club.example</p>
          <p>www.kvars-club.example</p>
        </div>
        <div class="contact-address">
          <p>42 Marwick Rd, Epsom</p>
          <p>Auckland 1051</p>
        </div>
      </div>
    </section>
  </main>
</body>
</html>
```